Biz Cards to match new logo

I'm looking for a business card layout to go with my new logo. I'd like to have one side in colour (purple, with the logo in white) and the other side to be white with the purple logo and contact info in black font: name, address (2 lines), phone, email, fax, website. The logo includes the company name so it doesn't need to be repeated in the text. The font should be legibile to the semi-blind. (I hate small fonts on business cards).

```html
<!DOCTYPE html>
<html lang="en">
<head>
<meta charset="utf-8">
<title>Corvina Labs – Business Cards</title>
<link rel="stylesheet" href="https://fonts.googleapis.com/css2?family=Questrial&display=swap">
<style>
  :root {
    --purple: #633479;
    --purple-deep: #552a6a;
    --lavender: #8d7a9b;
    --lavender-soft: #a596b0;
    --paper: #ffffff;
    --ink: #241a2a;
    --name-tint: #c9b6d6;
    --backdrop: #f3f2f5;
    --font: "Questrial", "Century Gothic", sans-serif;
  }
  * { box-sizing: border-box; margin: 0; padding: 0; }
  html, body {
    width: 1200px;
    height: 873px;
    overflow: hidden;
    background: var(--backdrop);
    font-family: var(--font);
  }
  .canvas {
    position: relative;
    width: 1200px;
    height: 873px;
  }
  .card {
    position: absolute;
    top: 286px;
    width: 520px;
    height: 300px;
    border-radius: 4px;
    overflow: hidden;
    box-shadow: 0 10px 28px rgba(40, 20, 50, 0.18);
  }
  .card--contact { left: 50px; background: var(--paper); }
  .card--brand { left: 630px; background: var(--purple); }

  .card__shapes {
    position: absolute;
    inset: 0;
    width: 100%;
    height: 100%;
  }

  .wordmark {
    position: absolute;
    display: flex;
    align-items: center;
    gap: 12px;
    font-size: 34px;
    letter-spacing: 0.08em;
    text-transform: uppercase;
    white-space: nowrap;
  }
  .wordmark__square {
    width: 22px;
    height: 22px;
  }
  .card--contact .wordmark {
    top: 54px;
    left: 150px;
    color: var(--purple);
  }
  .card--contact .wordmark__square { background: var(--purple); }

  .card--brand .wordmark {
    top: 50%;
    left: 50%;
    transform: translate(-50%, -50%);
    font-size: 42px;
    color: var(--paper);
  }
  .card--brand .wordmark__square { background: var(--paper); width: 26px; height: 26px; }

  .contact {
    position: absolute;
    left: 150px;
    top: 150px;
    list-style: none;
    font-size: 17px;
    line-height: 1.13;
    color: var(--ink);
  }
  .contact__name {
    color: var(--name-tint);
    letter-spacing: 0.06em;
    text-transform: uppercase;
    font-size: 16px;
    margin-bottom: 2px;
  }
</style>
</head>
<body>
  <main class="canvas">

    <section class="card card--contact" aria-label="Business card, contact side">
      <svg class="card__shapes" viewBox="0 0 520 300" preserveAspectRatio="none" aria-hidden="true">
        <path d="M0 300 L0 0 L90 0 C60 70 70 150 130 300 Z" fill="var(--lavender-soft)"/>
        <path d="M70 300 C40 230 40 180 60 130 L520 130 L520 300 Z" fill="var(--purple)"/>
      </svg>
      <div class="wordmark">
        <span class="wordmark__square"></span>
        <span class="wordmark__name">Corvina Labs</span>
      </div>
      <ul class="contact">
        <li class="contact__name">Name</li>
        <li>Address line 1</li>
        <li>Address line 2</li>
        <li>Phone</li>
        <li>Email</li>
        <li>Fax</li>
        <li>Website</li>
      </ul>
    </section>

    <section class="card card--brand" aria-label="Business card, brand side">
      <div class="wordmark">
        <span class="wordmark__square"></span>
        <span class="wordmark__name">Corvina Labs</span>
      </div>
    </section>

  </main>
</body>
</html>
```